Rebranding our business - Business Cards

We are currently rebranding our business and have just completed our new logo and now are wanting to have new business cards designed.

I will upload our old business card design as we would like to keep the same information on the card, Including the icon dot points on the back. I will also upload other designs I would like placed on the cards.. Such as a character,

I would like our power statement to be:
KTW Removals -The Gentle Movers.

Instead of: Allow KTW Removals To Carry the Weight Of Every Relocation,

I am happy for the designer to run with their own ideas.

```html
<!DOCTYPE html>
<html lang="en">
<head>
<meta charset="utf-8">
<title>KTW Removals – Business Cards</title>
<link rel="stylesheet" href="https://fonts.googleapis.com/css2?family=Open+Sans:wght@400;600;700&display=swap">
<style>
  :root{
    --navy:#2a2f7a;
    --navy-deep:#1b1f5c;
    --orange:#f26a2e;
    --blue:#2f8fd8;
    --white:#ffffff;
    --ink:#2a2d52;
    --grey-bg:#e9e9ec;
  }
  *{box-sizing:border-box;margin:0;padding:0}
  html,body{width:1200px;height:913px;overflow:hidden}
  body{background:var(--grey-bg);font-family:"Open Sans",Arial,sans-serif;position:relative}
  .card{position:absolute;width:540px;height:330px;border-radius:16px;overflow:hidden;box-shadow:0 6px 18px rgba(0,0,0,.18)}
  .card-front{left:60px;top:90px;background:var(--white)}
  .card-back{left:600px;top:480px;background:linear-gradient(160deg,#3a3f8e 0%,var(--navy) 45%,var(--navy-deep) 100%)}
  .card svg.bg{position:absolute;inset:0}
  .brand-name{position:absolute;font-weight:700;font-size:30px;color:var(--orange);letter-spacing:.3px;display:flex;align-items:center;gap:10px;white-space:nowrap}
  .brand-mark{width:13px;height:13px;background:var(--white);display:inline-block}
  .front-brand{left:40px;top:118px}
  .tagline{position:absolute;left:40px;top:190px;color:var(--white);line-height:1.4;white-space:nowrap}
  .tagline .company{color:var(--orange);font-size:14px;text-transform:uppercase;letter-spacing:.5px}
  .tagline .motto{font-size:15px;text-transform:uppercase;letter-spacing:.3px}
  .holder{position:absolute;right:26px;top:16px;text-align:right;white-space:nowrap}
  .holder .name{color:var(--white);font-weight:700;font-size:19px}
  .holder .role{color:var(--orange);font-size:13px}
  .contact-list{position:absolute;list-style:none;font-size:12px;color:var(--ink);white-space:nowrap}
  .contact-list li{display:flex;align-items:center;justify-content:flex-end;gap:8px;height:19px}
  .front-contacts{right:22px;top:112px}
  .icon{width:12px;height:12px;flex:none}
  .back-brand{left:36px;top:72px}
  .character{position:absolute;left:400px;top:14px;width:104px;height:110px;border-radius:12px;background:linear-gradient(180deg,#8a8dbd 0%,#e98f5a 60%,#6d70a8 100%)}
  .band{position:absolute;top:140px;height:24px;background:var(--orange);color:var(--white);font-size:12px;display:flex;align-items:center;padding:0 10px;white-space:nowrap}
  .band-provides{left:160px;width:190px;justify-content:flex-end}
  .band-insurance{left:354px;right:0;text-transform:uppercase;font-weight:600;font-size:11px}
  .services{position:absolute;right:200px;top:176px;list-style:none;color:var(--white);font-size:12px;text-align:right;white-space:nowrap}
  .services li{display:flex;align-items:center;justify-content:flex-end;gap:8px;height:20px}
  .back-contacts{left:356px;top:176px}
  .back-contacts li{justify-content:flex-start;color:var(--white);height:20px}
  .stripe-bottom{position:absolute;left:0;top:292px;width:346px;height:5px;background:var(--orange)}
</style>
</head>
<body>

<section class="card card-front">
  <svg class="bg" width="540" height="330" viewBox="0 0 540 330">
    <path d="M0 0 H540 V60 C400 62 320 110 300 190 C285 260 270 300 220 330 H0 Z" fill="var(--navy)"/>
    <path d="M540 60 C400 62 320 110 300 190 C285 260 270 300 220 330" transform="translate(-8 0)" fill="none" stroke="var(--blue)" stroke-width="6"/>
    <path d="M540 60 C400 62 320 110 300 190 C285 260 270 300 220 330" fill="none" stroke="var(--orange)" stroke-width="6"/>
  </svg>
  <div class="holder">
    <p class="name">Liam Carver</p>
    <p class="role">Owner Operator</p>
  </div>
  <div class="brand-name front-brand"><span class="brand-mark"></span>KTW Removals</div>
  <div class="tagline">
    <p class="company">KTW Removals</p>
    <p class="motto">The Gentle Movers</p>
  </div>
  <ul class="contact-list front-contacts">
    <li>Harbour Bay, QLD 4870</li>
    <li>0400 318 672
      <svg class="icon" viewBox="0 0 12 12"><rect x="3" y="0.5" width="6" height="11" rx="1.2" fill="none" stroke="var(--orange)"/></svg></li>
    <li>07 5500 2468
      <svg class="icon" viewBox="0 0 12 12"><path d="M2 3 C2 1 10 1 10 3 L9 5 H3 Z M2 6 H10 V11 H2 Z" fill="var(--orange)"/></svg></li>
    <li>ktwremovals@mailhub.com
      <svg class="icon" viewBox="0 0 12 12"><rect x="0.5" y="2" width="11" height="8" fill="none" stroke="var(--orange)"/><path d="M0.5 2 L6 7 L11.5 2" fill="none" stroke="var(--orange)"/></svg></li>
    <li>www.ktwremovals.com.au
      <svg class="icon" viewBox="0 0 12 12"><circle cx="6" cy="6" r="5" fill="none" stroke="var(--orange)"/><path d="M1 6 H11 M6 1 C3 4 3 8 6 11 M6 1 C9 4 9 8 6 11" fill="none" stroke="var(--orange)" stroke-width=".8"/></svg></li>
    <li>social/ktwremovals
      <svg class="icon" viewBox="0 0 12 12"><circle cx="6" cy="6" r="5" fill="var(--orange)"/></svg></li>
  </ul>
</section>

<section class="card card-back">
  <div class="brand-name back-brand"><span class="brand-mark"></span>KTW Removals</div>
  <div class="character" role="img" aria-label="Cartoon removalist character with a hand trolley and a box"></div>
  <div class="band band-provides">KTW Removals Provides:</div>
  <div class="band band-insurance">Free Transit Insurance</div>
  <ul class="services">
    <li>Local, Country &amp; Interstate Removals<svg class="icon" viewBox="0 0 12 12"><path d="M1 3 H7 V9 H1 Z M7 5 H10 L11 7 V9 H7 Z" fill="var(--orange)"/></svg></li>
    <li>Home &amp; Hi Rise Removals<svg class="icon" viewBox="0 0 12 12"><path d="M1 6 L6 1.5 L11 6 H9.5 V11 H2.5 V6 Z" fill="var(--orange)"/></svg></li>
    <li>Office &amp; Factory Relocations<svg class="icon" viewBox="0 0 12 12"><rect x="2" y="1" width="8" height="10" fill="var(--orange)"/></svg></li>
    <li>Pre - Packing &amp; Unpacking Service's<svg class="icon" viewBox="0 0 12 12"><rect x="1.5" y="3" width="9" height="8" fill="var(--orange)"/></svg></li>
    <li>Storage Solution<svg class="icon" viewBox="0 0 12 12"><path d="M1 4 L6 1 L11 4 V11 H1 Z" fill="var(--orange)"/></svg></li>
  </ul>
  <ul class="contact-list back-contacts">
    <li><svg class="icon" viewBox="0 0 12 12"><rect x="3" y="0.5" width="6" height="11" rx="1.2" fill="none" stroke="var(--orange)"/></svg>0400 318 672</li>
    <li><svg class="icon" viewBox="0 0 12 12"><path d="M2 3 C2 1 10 1 10 3 L9 5 H3 Z M2 6 H10 V11 H2 Z" fill="var(--orange)"/></svg>07 5500 2468</li>
    <li><svg class="icon" viewBox="0 0 12 12"><rect x="0.5" y="2" width="11" height="8" fill="none" stroke="var(--orange)"/><path d="M0.5 2 L6 7 L11.5 2" fill="none" stroke="var(--orange)"/></svg>ktwremovals@mailhub.com</li>
    <li><svg class="icon" viewBox="0 0 12 12"><circle cx="6" cy="6" r="5" fill="none" stroke="var(--orange)"/><path d="M1 6 H11 M6 1 C3 4 3 8 6 11 M6 1 C9 4 9 8 6 11" fill="none" stroke="var(--orange)" stroke-width=".8"/></svg>www.ktwremovals.com.au</li>
  </ul>
  <div class="stripe-bottom"></div>
</section>

</body>
</html>
```